Law Office business card design

I have a general practice specializing in criminal defense work and domestic cases. I have extensive trial and appellate experience.

Target Market(s)

general public

Industry/Entity Type

Defense

Contact Information for Business Card

Dorrington Law Office, P.A.
382 N. 4th
PO Box 5284
Salina, KS 67409-5284
(785) 555-0172
(785) 555-0198 FAX
tdorrin@quellmail.net

Requirements
Must have
• A symbol that immediately identifes the card as a legal practice.

```html
<!DOCTYPE html>
<html lang="en">
<head>
<meta charset="utf-8">
<title>Dorrington Law Office, P.A. — Business Card</title>
<link rel="stylesheet" href="https://fonts.googleapis.com/css2?family=EB+Garamond:wght@400&display=swap">
<style>
  :root {
    --card-black: #000000;
    --stone-dark: #2a2724;
    --stone-mid: #4a4640;
    --stone-light: #6b655c;
    --ink-white: #ffffff;
    --wood-light: #b8784a;
    --wood-dark: #6e3a1c;
  }
  html, body {
    margin: 0;
    padding: 0;
    width: 1200px;
    height: 702px;
    overflow: hidden;
    background: var(--card-black);
  }
  .business-card {
    position: relative;
    width: 1200px;
    height: 702px;
    background: var(--card-black);
    overflow: hidden;
    font-family: "EB Garamond", Garamond, serif;
    color: var(--ink-white);
  }
  .card-art {
    position: absolute;
    inset: 0;
  }
  .firm-name {
    position: absolute;
    left: 63px;
    top: 98px;
    margin: 0;
    font-size: 60px;
    font-weight: 400;
    line-height: 1;
    letter-spacing: 0.3px;
    white-space: nowrap;
  }
  .street-address {
    position: absolute;
    left: 88px;
    top: 237px;
    margin: 0;
    font-size: 42px;
    line-height: 1;
    white-space: nowrap;
  }
  .contact-list {
    position: absolute;
    left: 86px;
    top: 459px;
    margin: 0;
    padding: 0;
    list-style: none;
    font-size: 34px;
    line-height: 42px;
    white-space: nowrap;
  }
</style>
</head>
<body>
  <main class="business-card">
    <svg class="card-art" width="1200" height="702" viewBox="0 0 1200 702">
      <defs>
        <linearGradient id="stone-band" x1="0" y1="0" x2="1" y2="1">
          <stop offset="0" stop-color="var(--stone-mid)"/>
          <stop offset="0.5" stop-color="var(--stone-light)"/>
          <stop offset="1" stop-color="var(--stone-dark)"/>
        </linearGradient>
        <linearGradient id="wood-tone" x1="0" y1="0" x2="1" y2="1">
          <stop offset="0" stop-color="var(--wood-light)"/>
          <stop offset="1" stop-color="var(--wood-dark)"/>
        </linearGradient>
      </defs>
      <rect class="stone-band-horizontal" x="0" y="160" width="1200" height="63" fill="url(#stone-band)"/>
      <polygon class="stone-band-diagonal" points="686,0 774,0 1150,702 1056,702" fill="url(#stone-band)"/>
      <rect class="gavel-illustration" role="img" aria-label="Illustration of a wooden judge's gavel with a gold band, resting on its sound block" x="752" y="50" width="371" height="515" rx="60" fill="url(#wood-tone)"/>
    </svg>

    <h1 class="firm-name">Dorrington Law Office, P.A</h1>
    <p class="street-address">382 N. 4th PO Box 5284 Salina</p>
    <ul class="contact-list">
      <li class="contact-zip">KS 67409-5284</li>
      <li class="contact-phone">(785) 555-0172</li>
      <li class="contact-fax">(785) 555-0198 FAX</li>
      <li class="contact-email">tdorrin@quellmail.net</li>
    </ul>
  </main>
</body>
</html>
```